Diet product based by mushroom

My company name is HealtHomeIt means heal + home(healing & safe)Our target is women who are twenties - thirties having job & desire to lose weight within short terms about a week, two weeks, a monthMy company makes diet product based on mushrooms So we are looking for this packaging design of black mushroom + enoki mushroom. This product consists of one set(10 stick - each stick 3g) My company's main color is pastel yellow wish & white and company's mission is whoever we make relationship helps their life with mentally, physically We would like to see designs that use the color of our company logoThank you

Target Market(s)

Women who are twenties, thirties having job & desire to lose weight within short terms about a week, two weeks, a month

Colors
f6faec
eaf2ce
cadf82
abd036
9bcb3b

Requirements
Must have
• My project must have logo's color, the word (다온채, the food of gods')
• simple
Nice to have
• simple & highlight,legibility, simple&white
Should not have
• unbalance

```html
<!DOCTYPE html>
<html lang="en">
<head>
<meta charset="utf-8">
<title>다온채 — Mushroom stick packaging</title>
<link rel="stylesheet" href="https://fonts.googleapis.com/css2?family=Nanum+Gothic:wght@400;700&family=Open+Sans:wght@300;600&family=Eagle+Lake&display=swap">
<style>
  :root {
    --page: #f3f3f1;
    --paper: #fbfbfa;
    --ink-grey: #5e5e5e;
    --leaf-deep: #3d7a43;
    --leaf-band: #437f47;
    --leaf-light: #9bcb3b;
    --leaf-pale: #cadf82;
    --leaf-mist: #eaf2ce;
    --sky-teal: #5aa3a0;
    --crimp: #dcdcdc;
    --cream: #f6faec;
  }
  * { box-sizing: border-box; margin: 0; padding: 0; }
  html, body { width: 1200px; height: 986px; overflow: hidden; background: var(--page); }
  .canvas { position: relative; width: 1200px; height: 986px; }

  /* Box front panel */
  .box-front {
    position: absolute; left: 110px; top: 100px; width: 400px; height: 790px;
    background: var(--paper); box-shadow: 0 2px 10px rgba(0,0,0,.08); overflow: hidden;
  }
  .brand-word { font-family: "Nanum Gothic", sans-serif; font-weight: 400; color: var(--ink-grey); text-align: center; letter-spacing: 6px; }
  .tagline { font-family: "Open Sans", sans-serif; font-weight: 300; color: var(--ink-grey); text-align: center; letter-spacing: 1px; }
  .box-front .brand-word { margin-top: 54px; font-size: 72px; line-height: 1; }
  .box-front .tagline { margin-top: 10px; font-size: 19px; }

  .forest-art {
    position: absolute; left: 0; right: 0;
    background: radial-gradient(ellipse at 50% 55%, var(--leaf-pale) 0%, var(--leaf-mist) 55%, rgba(234,242,206,0) 80%);
  }
  .box-front .forest-art { top: 180px; height: 330px; }

  .logo-lockup { position: absolute; left: 0; right: 0; display: flex; flex-direction: column; align-items: center; }
  .logo-dot { border-radius: 50%; background: radial-gradient(circle at 40% 30%, var(--sky-teal), var(--leaf-light) 70%); }
  .logo-name { font-family: "Open Sans", sans-serif; font-weight: 300; color: var(--leaf-deep); letter-spacing: 3px; line-height: 1.2; }
  .logo-line { font-family: "Nanum Gothic", sans-serif; color: var(--leaf-deep); line-height: 1.2; }
  .box-front .logo-lockup { top: 228px; }
  .box-front .logo-dot { width: 180px; height: 180px; }
  .box-front .logo-name { margin-top: 12px; font-size: 30px; }
  .box-front .logo-line { margin-top: 4px; font-size: 13px; }

  .flavour-band {
    position: absolute; left: 0; right: 0; bottom: 0; height: 280px;
    background: var(--leaf-band); color: var(--cream); text-align: center;
  }
  .band-dots { position: absolute; left: 36px; right: 36px; border-top: 3px dotted rgba(246,250,236,.8); }
  .band-title { font-family: "Eagle Lake", cursive; color: var(--cream); }
  .band-sub { font-family: "Open Sans", sans-serif; font-weight: 300; color: var(--leaf-light); }
  .box-front .band-title { position: absolute; top: 92px; left: 0; right: 0; font-size: 58px; }
  .box-front .band-sub { position: absolute; top: 170px; left: 0; right: 0; font-size: 21px; }

  /* Stick sachets */
  .stick {
    position: absolute; top: 140px; width: 160px; height: 730px;
    background: var(--paper); box-shadow: 0 2px 8px rgba(0,0,0,.08); overflow: hidden;
  }
  .stick .crimp { position: absolute; left: 0; right: 0; height: 22px; background: repeating-linear-gradient(90deg, var(--crimp) 0 2px, #ececec 2px 4px); }
  .stick .crimp.top { top: 0; } .stick .crimp.bottom { bottom: 0; }
  .stick .brand-word { margin-top: 46px; font-size: 40px; letter-spacing: 3px; line-height: 1.1; }
  .stick .tagline { margin-top: 4px; font-size: 11px; }
  .stick .forest-art { top: 118px; height: 300px; }
  .stick .logo-lockup { top: 130px; }
  .stick .logo-dot { width: 104px; height: 104px; }
  .stick .logo-name { margin-top: 6px; font-size: 16px; letter-spacing: 1px; }
  .stick .logo-line { margin-top: 2px; font-size: 9px; }
  .stick-flavour {
    position: absolute; top: 292px; left: 0; right: 0; text-align: center;
    font-family: "Open Sans", sans-serif; font-weight: 600; font-size: 14px; line-height: 1.25; color: #2f3a2f;
  }
  .stick .flavour-band { height: 290px; bottom: 22px; }
  .stick-label {
    position: absolute; left: 50%; top: 50%; width: 270px; transform: translate(-50%,-50%) rotate(-90deg);
    text-align: left;
  }
  .stick .band-title { font-size: 44px; line-height: 1; }
  .stick .band-sub { font-size: 14px; margin-top: 4px; }
</style>
</head>
<body>
<main class="canvas">

  <section class="box-front">
    <h1 class="brand-word">다온채</h1>
    <p class="tagline">THE FOOD OF GODS</p>
    <div class="forest-art" role="img" aria-label="Green line illustration of forest, clouds and mushrooms"></div>
    <div class="logo-lockup">
      <div class="logo-dot"></div>
      <p class="logo-name">Zanterwik</p>
      <p class="logo-line">가볍게 건강한 하루</p>
    </div>
    <div class="flavour-band">
      <div class="band-dots" style="top:66px"></div>
      <p class="band-title">Mushroom</p>
      <p class="band-sub">rapid weight loss secret</p>
      <div class="band-dots" style="top:228px"></div>
    </div>
  </section>

  <section class="stick" style="left:620px">
    <div class="crimp top"></div>
    <h2 class="brand-word">다온채</h2>
    <p class="tagline">THE FOOD OF GODS</p>
    <div class="forest-art" role="img" aria-label="Green line illustration of forest and mushrooms"></div>
    <div class="logo-lockup"><div class="logo-dot"></div><p class="logo-name">Zanterwik</p><p class="logo-line">가볍게 건강한 하루</p></div>
    <p class="stick-flavour">Black<br>mushroom<br>+<br>Enoki<br>mushroom</p>
    <div class="flavour-band"><div class="stick-label"><p class="band-title">Mushroom</p><p class="band-sub">rapid weight loss secret</p></div></div>
    <div class="crimp bottom"></div>
  </section>

  <section class="stick" style="left:800px">
    <div class="crimp top"></div>
    <h2 class="brand-word">다온채</h2>
    <p class="tagline">THE FOOD OF GODS</p>
    <div class="forest-art" role="img" aria-label="Green line illustration of forest and mushrooms"></div>
    <div class="logo-lockup"><div class="logo-dot"></div><p class="logo-name">Zanterwik</p><p class="logo-line">가볍게 건강한 하루</p></div>
    <p class="stick-flavour">Black<br>mushroom<br>+<br>Enoki<br>mushroom</p>
    <div class="flavour-band"><div class="stick-label"><p class="band-title">Mushroom</p><p class="band-sub">rapid weight loss secret</p></div></div>
    <div class="crimp bottom"></div>
  </section>

  <section class="stick" style="left:980px">
    <div class="crimp top"></div>
    <h2 class="brand-word">다온채</h2>
    <p class="tagline">THE FOOD OF GODS</p>
    <div class="forest-art" role="img" aria-label="Green line illustration of forest and mushrooms"></div>
    <div class="logo-lockup"><div class="logo-dot"></div><p class="logo-name">Zanterwik</p><p class="logo-line">가볍게 건강한 하루</p></div>
    <p class="stick-flavour">Black<br>mushroom<br>+<br>Enoki<br>mushroom</p>
    <div class="flavour-band"><div class="stick-label"><p class="band-title">Mushroom</p><p class="band-sub">rapid weight loss secret</p></div></div>
    <div class="crimp bottom"></div>
  </section>

</main>
</body>
</html>
```